Chewing Gum With Active Ingredients Needs Packaging Design

Brivella Mint Systems is a revolutionary new chewing gum that contains active ingredients commonly found in mouthwashes - it's a portable and convenient way to keep a fresh, clean, and healthy mouth. We have a thorough design brief (attached file) for the packaging we need - a simple sleeve for blister packed gum. We want our design to convey that we are a modern, effective, and high-end product.

Target Market(s)

Young professionals, 20-35 years old

Font styles to use
Serif
Sans Serif

Colors
0292cd
ffffff
0555a3

Requirements
Must have
• A sleek, elegant design
• ALL of the elements listed in the creative brief PDF
• Attached logo
Nice to have
• Incorporation of foil into the design
• A unique, unmistakable look
Should not have
• Too medical of a look

```html
<!DOCTYPE html>
<html lang="en">
<head>
<meta charset="utf-8">
<title>Brivella Mint Systems – Gum Sleeve Dieline</title>
<link href="https://fonts.googleapis.com/css2?family=Saira:wght@300;400;500&family=Saira+Semi+Condensed:wght@400;500&family=Arimo:wght@400;700&display=swap" rel="stylesheet">
<style>
  :root {
    --canvas: #ffffff;
    --ink: #0c0c0d;
    --panel: #151516;
    --panel-edge: #232325;
    --band: #1c1c1d;
    --orange: #ff8a1c;
    --orange-deep: #c24a05;
    --white: #ffffff;
    --silver: #d9d9dc;
    --grey-text: #bfbfc3;
    --dash: #e39a3c;
    --trim: #43a8d8;
    --glue: #e3e4e6;
    --warn: #e0171d;
  }
  * { box-sizing: border-box; margin: 0; padding: 0; }
  html, body { width: 800px; height: 1200px; overflow: hidden; background: var(--canvas); }
  .canvas { position: relative; width: 800px; height: 1200px; }

  .dieline {
    position: absolute; left: 20px; top: 73px; width: 760px; height: 1054px;
    border: 1px solid var(--trim); overflow: hidden; background: var(--ink);
  }

  /* ---------- back panel (printed upside down) ---------- */
  .back-panel {
    position: absolute; left: 0; top: 0; width: 760px; height: 450px;
    transform: rotate(180deg);
    background:
      radial-gradient(ellipse 160px 60px at 700px 230px, rgba(255,138,28,.55), transparent 70%),
      linear-gradient(200deg, #262628 0%, var(--panel) 45%, #0e0e0f 100%);
    font-family: "Saira Semi Condensed", sans-serif; color: var(--white);
  }
  .drug-facts {
    position: absolute; left: 119px; top: 32px; width: 192px; height: 327px;
    background: var(--white); color: #111; border: 2px solid var(--white);
    font-family: "Arimo", sans-serif; font-size: 6.4px; line-height: 1.35; padding: 3px 4px;
  }
  .drug-facts h3 { font-size: 11px; font-style: italic; font-weight: 700; border-bottom: 3px solid #111; }
  .drug-facts .row { display: flex; justify-content: space-between; }
  .drug-facts .head { font-weight: 700; font-style: italic; font-size: 7.5px; border-bottom: 1px solid #111; margin-top: 2px; }
  .drug-facts .active { background: #7a2a12; color: var(--white); padding: 1px 2px; margin: 1px -4px 0; padding-left: 6px; padding-right: 6px; border-bottom: 3px solid #111; }
  .drug-facts ul { list-style: none; padding-left: 2px; }
  .drug-facts li::before { content: "■ "; }
  .drug-facts .rule { border-bottom: 3px solid #111; margin: 2px -4px; }

  .claim {
    position: absolute; left: 331px; top: 64px; font-size: 15.5px; line-height: 1.33;
    letter-spacing: .3px; text-transform: uppercase;
  }
  .distributor { position: absolute; left: 331px; top: 195px; font-size: 14px; line-height: 1.35; text-transform: uppercase; }
  .feature-icons { position: absolute; left: 331px; top: 252px; display: flex; gap: 9px; }
  .feature-icons svg { width: 40px; height: 40px; }
  .care-icons { position: absolute; left: 540px; top: 244px; display: flex; gap: 8px; }
  .care-icons svg { width: 32px; height: 32px; }
  .site { position: absolute; left: 331px; top: 392px; font-size: 14.5px; letter-spacing: .6px; }

  .tuck { position: absolute; top: 0; left: 0; }

  /* ---------- plaque band ---------- */
  .stat-band {
    position: absolute; left: 0; top: 450px; width: 760px; height: 53px;
    transform: rotate(180deg);
    background:
      linear-gradient(90deg, transparent 0%, transparent 65%, rgba(255,138,28,.75) 80%, rgba(194,74,5,.5) 92%, transparent 100%),
      linear-gradient(90deg, rgba(255,138,28,.55), transparent 14%),
      var(--band);
    border-top: 1px dashed #555; border-bottom: 1px dashed #555;
    display: flex; align-items: center; padding-left: 60px; gap: 14px;
    font-family: "Saira", sans-serif; font-weight: 400; color: var(--white);
    font-size: 17px; letter-spacing: 2.4px; text-transform: uppercase;
  }
  .mark-dot { width: 28px; height: 28px; border: 2px solid var(--white); border-radius: 50%; flex: none; }

  /* ---------- front panel ---------- */
  .front-panel {
    position: absolute; left: 0; top: 503px; width: 760px; height: 497px;
    background:
      radial-gradient(ellipse 420px 90px at 300px 300px, rgba(255,138,28,.45), transparent 70%),
      linear-gradient(115deg, transparent 30%, rgba(255,138,28,.18) 42%, transparent 52%),
      linear-gradient(200deg, #2a2a2c 0%, var(--panel) 40%, #0c0c0d 100%);
    font-family: "Saira", sans-serif; color: var(--white);
  }
  .flame-accent {
    position: absolute; left: 0; top: 170px; width: 760px; height: 327px;
    background:
      radial-gradient(ellipse 260px 40px at 240px 170px, rgba(255,150,40,.7), transparent 70%),
      radial-gradient(ellipse 140px 200px at 380px 70px, rgba(255,120,20,.35), transparent 70%),
      radial-gradient(ellipse 120px 60px at 700px 300px, rgba(255,120,20,.45), transparent 70%);
  }
  .pack-info {
    position: absolute; right: 44px; top: 24px; text-align: right;
    font-size: 17.5px; line-height: 1.3; letter-spacing: .4px; color: var(--silver); text-transform: uppercase;
  }
  .brand { position: absolute; left: 195px; top: 268px; display: flex; align-items: center; gap: 16px; }
  .brand-ring { width: 94px; height: 94px; border: 4px solid var(--silver); border-radius: 50%; }
  .brand-name {
    font-weight: 300; font-size: 62px; line-height: 1; letter-spacing: 6px; color: var(--silver); text-transform: uppercase;
  }
  .brand-sub {
    position: absolute; left: 310px; top: 347px; font-weight: 300; font-size: 15px;
    letter-spacing: 16.5px; color: var(--silver); text-transform: uppercase;
  }
  .benefits {
    position: absolute; right: 44px; top: 382px; display: grid; grid-template-columns: auto auto;
    column-gap: 22px; font-size: 17px; line-height: 1.28; text-transform: uppercase; color: var(--silver);
  }
  .benefits span:nth-child(odd) { text-align: right; }
  .gum-art {
    position: absolute; left: 35px; top: 318px; width: 112px; height: 110px; border-radius: 18px;
    background: radial-gradient(circle at 40% 35%, #ffffff, #d6d6d8 60%, rgba(200,200,205,0) 75%);
  }
  .tagline {
    position: absolute; left: 55px; top: 452px; display: flex; align-items: center; gap: 18px;
    font-size: 17px; letter-spacing: 3.2px; color: var(--silver); text-transform: uppercase;
  }
  .tagline .mark-dot { width: 30px; height: 30px; border-color: var(--silver); }

  .glue-area {
    position: absolute; left: 0; top: 1000px; width: 760px; height: 54px; background: var(--glue);
    display: flex; align-items: center; padding-left: 84px; gap: 8px;
    font-family: "Arimo", sans-serif; font-size: 15.5px; color: var(--warn);
  }
  .guides { position: absolute; left: 0; top: 0; pointer-events: none; }
</style>
</head>
<body>
<div class="canvas">
  <div class="dieline">

    <section class="back-panel">
      <div class="drug-facts">
        <h3>Drug Facts</h3>
        <div class="row head"><span>Active ingredient (in each piece)</span><span>Purpose</span></div>
        <div class="row active"><span>Xylitol 500 mg</span><span>Breath freshener</span></div>
        <div class="head">Uses</div>
        <ul>
          <li>temporarily freshens breath</li>
          <li>helps reduce plaque</li>
          <li>helps protect gums</li>
          <li>whitens teeth</li>
        </ul>
        <div class="rule"></div>
        <div class="head">Warnings</div>
        <p>Not for children under 6.</p>
        <p>Stop use if irritation occurs.</p>
        <p><b>Do not use</b></p>
        <ul>
          <li>with other oral rinse products</li>
          <li>if allergic to any ingredient</li>
        </ul>
        <p><b>Ask a dentist before use if you have gum disease.</b></p>
        <p>Keep out of reach of children.</p>
      </div>

      <p class="claim">With FDA-approved active ingredients,<br>dentist-recommended Brivella gum<br>whitens teeth, freshens breath,<br>and helps reduce plaque<br>and prevent gingivitis</p>
      <p class="distributor">Dist by Larkfield Goods:<br>Boulder, CO questions?<br>XXX-XXX-XXXX</p>

      <div class="feature-icons">
        <svg viewBox="0 0 40 40"><rect width="40" height="40" rx="9" fill="#fff"/><circle cx="20" cy="20" r="10" fill="none" stroke="#111" stroke-width="3"/></svg>
        <svg viewBox="0 0 40 40"><rect width="40" height="40" rx="9" fill="#fff"/><path d="M20 9v22M12 17h16" stroke="#111" stroke-width="4"/></svg>
        <svg viewBox="0 0 40 40"><rect width="40" height="40" rx="9" fill="#fff"/><path d="M11 28l9-16 9 16z" fill="#111"/></svg>
      </div>

      <div class="care-icons">
        <svg viewBox="0 0 32 32"><circle cx="16" cy="16" r="13" fill="none" stroke="#fff" stroke-width="3"/><path d="M7 7l18 18" stroke="#fff" stroke-width="3"/></svg>
        <svg viewBox="0 0 32 32"><path d="M10 28V10h6v18M18 14h5v14" fill="none" stroke="#fff" stroke-width="3"/></svg>
      </div>

      <p class="site">WWW.BRIVELLAGUM.COM</p>

      <svg class="tuck" width="760" height="450" viewBox="0 0 760 450">
        <path d="M0 146 a60 60 0 0 1 0 120" fill="none" stroke="var(--dash)" stroke-width="1.4" stroke-dasharray="6 4"/>
        <path d="M760 146 a60 60 0 0 0 0 120" fill="none" stroke="var(--dash)" stroke-width="1.4" stroke-dasharray="6 4"/>
      </svg>
    </section>

    <section class="stat-band">
      <span class="mark-dot"></span>
      <span>2 in 3 adults have visible plaque</span>
    </section>

    <section class="front-panel">
      <div class="flame-accent" role="img" aria-label="Glowing orange light streaks across the dark pack"></div>
      <p class="pack-info">8 pieces sugar free gum<br>aspartame free with xylitol<br>peppermint</p>
      <div class="brand">
        <span class="brand-ring"></span>
        <span class="brand-name">Brivella</span>
      </div>
      <p class="brand-sub">Mint Systems</p>
      <div class="gum-art" role="img" aria-label="Two white gum pellets"></div>
      <div class="benefits">
        <span>Whitens teeth</span><span>Freshens breath</span>
        <span>Helps reduce plaque</span><span>Helps protect gums</span>
      </div>
      <div class="tagline"><span class="mark-dot"></span><span>Confidence guaranteed</span></div>
    </section>

    <div class="glue-area">
      <svg width="10" height="44" viewBox="0 0 10 44"><path d="M5 2v40M1 7l4-5 4 5M1 37l4 5 4-5" fill="none" stroke="#111" stroke-width="1.3"/></svg>
      <span>NO TEXT OR ART HERE IN GRAY AREA - packaging adhesive will be applied here!</span>
    </div>

    <svg class="guides" width="760" height="1054" viewBox="0 0 760 1054">
      <rect x="18" y="18" width="724" height="1018" fill="none" stroke="var(--dash)" stroke-width="1.2" stroke-dasharray="6 4"/>
    </svg>
  </div>
</div>
</body>
</html>
```